Darrel K. Holloway, MD

I would like to set up a web page for my new psychiatric practice. It should summarize my credentials and approach to care plus a patient portal to complete forms before appointments.
I am uploading a powerpoint with my contact information along with the color palette and format I would like to use. The email on the slide has not been reserved and I will need to reserve the domain as part of this process.

```html
<!DOCTYPE html>
<html lang="en">
<head>
<meta charset="utf-8">
<title>Calvera Psychiatric Practice</title>
<link href="https://fonts.googleapis.com/css2?family=PT+Serif:ital@0;1&family=Roboto:wght@400;500;700&display=swap" rel="stylesheet">
<style>
:root{
  --navy:#0c2e66;
  --navy-deep:#082350;
  --blue:#1a78f2;
  --panel:#ffffff;
  --page:#f1f1f1;
  --ink:#111;
  --muted:#555;
  --line:#d9d9d9;
}
*{margin:0;padding:0;box-sizing:border-box}
html,body{width:955px;height:1200px;overflow:hidden}
body{position:relative;background:var(--page);font-family:"Roboto",sans-serif;color:var(--ink)}
.abs{position:absolute}
.header{left:0;top:0;width:955px;height:512px;background:radial-gradient(ellipse at 50% 20%,#1c4f9a 0%,var(--navy) 55%,var(--navy-deep) 100%)}
.brand-mark{left:54px;top:40px;width:26px;height:26px;border-radius:50%;background:#3aa0ff}
.brand-name{left:90px;top:36px;font-family:"PT Serif",serif;font-size:32px;color:#fff;line-height:1}
.slogan{left:98px;top:75px;font-family:"PT Serif",serif;font-style:italic;font-size:12px;color:#fff}
.contact{font-family:"PT Serif",serif;font-size:14px;line-height:15px;color:#fff}
.nav{left:46px;top:112px;width:860px;height:40px;background:linear-gradient(#2a8cff,#0f6de6);display:flex}
.nav a{display:flex;align-items:center;justify-content:center;height:40px;color:#fff;font-size:9.5px;text-decoration:none;border-right:1px solid #0a5cc8}
.search{left:744px;top:124px;width:124px;height:18px;background:#0d63d6;color:#dfeeff;font-size:9px;display:flex;align-items:center;padding-left:22px}
.hero-photo{left:46px;top:153px;width:860px;height:320px;background:linear-gradient(180deg,#cfe6f2 0%,#e9f2f7 45%,#9fbddb 100%)}
.hero-band{left:46px;top:400px;width:860px;height:112px}
.hero-title{left:46px;top:470px;width:860px;text-align:center;font-family:"PT Serif",serif;font-size:22px;color:#fff;display:flex;align-items:center;justify-content:center;gap:8px}
.hero-title i{display:block;width:156px;height:4px;border-top:1px solid #bcd9ff;border-bottom:1px solid #bcd9ff}
.content{left:46px;top:512px;width:860px;height:324px;background:var(--panel);border-bottom:1px solid var(--line)}
.kicker{font-size:12.5px;color:var(--muted)}
.heading{font-size:18px;font-weight:400;color:#111;letter-spacing:.2px}
.body-text{font-size:8.8px;line-height:14.5px;color:#444}
.btn{width:74px;height:22px;background:var(--blue);color:#fff;font-size:9px;display:flex;align-items:center;justify-content:center}
.photo{background:linear-gradient(135deg,#b9c7cc,#6fa59b 50%,#4b6a88)}
.field{width:244px;height:25px;border:1px solid #ddd;border-radius:3px;background:#f4f4f4;font-size:9px;color:#777;padding-left:10px;display:flex;align-items:center}
.news{left:685px;width:210px;font-size:8.8px;line-height:12px;color:#444;display:flex;gap:8px}
.news b{flex:none;width:10px;height:10px;background:var(--blue);border-radius:2px;position:relative;margin-top:1px}
.news b::before,.news b::after{content:"";position:absolute;background:#fff}
.news b::before{left:2px;top:4px;width:6px;height:2px}
.news b::after{left:4px;top:2px;width:2px;height:6px}
.portrait{width:96px;height:96px;border-radius:50%;border:2px solid #fff;background:linear-gradient(#eef2f5,#9fc0de)}
.staff-name{font-size:14px;font-weight:500}
.staff-text{font-size:8.8px;line-height:14.5px;color:#555}
.footer{left:0;top:966px;width:955px;height:172px;background:#f6f6f6}
.foot-col h4{font-size:12.5px;font-weight:500;margin-bottom:5px}
.foot-col p{font-size:8.8px;line-height:19.2px;color:#444}
.foot-col.address p{line-height:14.5px}
.foot-photo{left:745px;top:978px;width:160px;height:160px;background:linear-gradient(180deg,#f6f6f6,#bcd3e2 60%,#5fb6c9)}
.bottom{left:0;top:1138px;width:955px;height:62px;background:var(--navy);color:#fff;font-size:8.8px;display:flex;align-items:center;justify-content:center}
</style>
</head>
<body>
<header class="abs header"></header>
<div class="abs brand-mark"></div>
<div class="abs brand-name">Calvera</div>
<div class="abs slogan">You slogan here</div>

<svg class="abs" style="left:294px;top:53px" width="20" height="24" viewBox="0 0 20 24" fill="none" stroke="#fff" stroke-width="1.4"><rect x="1" y="3" width="18" height="20" rx="2"/><rect x="4" y="1" width="4" height="20" rx="1"/><path d="M11 8h5M11 12h2M14 12h2M11 15h2M14 15h2M11 18h2M14 18h2"/></svg>
<div class="abs contact" style="left:324px;top:52px">CALL NOW FREE<br>858-555-0172</div>
<svg class="abs" style="left:515px;top:58px" width="22" height="15" viewBox="0 0 22 15" fill="none" stroke="#fff" stroke-width="1.4"><rect x="1" y="1" width="20" height="13"/><path d="M1 1l10 8 10-8M1 14l7-6M21 14l-7-6"/></svg>
<div class="abs contact" style="left:544px;top:52px">EMAIL :<br>CARE@CALVERAMD.COM</div>

<nav class="abs nav">
  <a style="width:68px">HOME</a>
  <a style="width:112px">CARE &amp; SERVICES</a>
  <a style="width:93px">OUR DOCTOR</a>
  <a style="width:98px">FORPATIENTS</a>
  <a style="width:97px">FOR VISITORS</a>
  <a style="width:132px">HEALTH INFORMATION</a>
  <a style="width:80px">ABOUT US</a>
</nav>
<div class="abs search">Search...</div>
<svg class="abs" style="left:750px;top:128px" width="10" height="10" viewBox="0 0 10 10" fill="none" stroke="#fff" stroke-width="1.5"><circle cx="4" cy="4" r="3"/><path d="M6.5 6.5L9.5 9.5"/></svg>

<div class="abs hero-photo" role="img" aria-label="Group of smiling doctors and nurses in white coats and scrubs"></div>
<svg class="abs hero-band" viewBox="0 0 860 112" preserveAspectRatio="none"><path d="M0 19 Q430 80 860 17 V112 H0Z" fill="#1677f5"/></svg>
<div class="abs hero-title"><i></i>PSYCHIATRIC PRACTICE<i></i></div>

<main class="abs content"></main>
<div class="abs kicker" style="left:69px;top:536px">Credentials &amp; Care</div>
<div class="abs heading" style="left:69px;top:551px">OUR APPROACH</div>
<div class="abs photo" style="left:69px;top:581px;width:271px;height:137px" role="img" aria-label="Care team in scrubs standing in a clinic corridor"></div>
<p class="abs body-text" style="left:69px;top:728px;width:256px">Darrel K. Holloway, MD, MBA is a board-certified psychiatrist offering evaluation, medication care and talk therapy. Visits are calm and unhurried, and each plan is built together ...</p>
<div class="abs btn" style="left:68px;top:784px">READ MORE</div>

<div class="abs kicker" style="left:392px;top:536px">Before Your Visit</div>
<div class="abs heading" style="left:392px;top:551px">PATIENT FORMS</div>
<p class="abs body-text" style="left:390px;top:585px;width:245px">Use the patient portal to complete intake forms, health history and consent before your first appointment. Returning patients can update medications, insurance and contact details online to save time ...</p>
<div class="abs" style="left:391px;top:665px;font-size:13.5px;font-weight:500">Patient portal login</div>
<div class="abs field" style="left:391px;top:699px">Enter Your User Name</div>
<div class="abs field" style="left:391px;top:732px">Password</div>
<div class="abs btn" style="left:391px;top:784px">START FORMS</div>

<div class="abs kicker" style="left:686px;top:536px">Today's</div>
<div class="abs heading" style="left:686px;top:551px">HEALTH NEWS</div>
<div class="abs news" style="top:592px"><b></b><span>Low Vitamin D Levels Linked to Weight Gain in Older Women</span></div>
<div class="abs news" style="top:629px"><b></b><span>Secondhand Smoke Linked to Raised Diabetes Risk</span></div>
<div class="abs news" style="top:666px"><b></b><span>Discovery of 'Master Molecule' Could Improve Stem Cell...</span></div>
<div class="abs news" style="top:703px"><b></b><span>Low Vitamin D Levels Linked to Weight Gain in Older Women</span></div>
<div class="abs news" style="top:740px"><b></b><span>Low Vitamin D Levels Linked to Weight Gain in Older Women</span></div>
<div class="abs btn" style="left:686px;top:784px">READ MORE</div>

<div class="abs portrait" style="left:46px;top:855px" role="img" aria-label="Portrait of a doctor in blue scrubs"></div>
<div class="abs staff-name" style="left:163px;top:877px">Marcus Ellery</div>
<p class="abs staff-text" style="left:163px;top:894px;width:160px">Secondhand Smoke Linked to Raised Diabetes Risk Discovery....</p>
<div class="abs portrait" style="left:344px;top:855px" role="img" aria-label="Portrait of a female doctor with stethoscope"></div>
<div class="abs staff-name" style="left:461px;top:877px">Nina Carvell</div>
<p class="abs staff-text" style="left:461px;top:894px;width:160px">Secondhand Smoke Linked to Raised Diabetes Risk Discovery....</p>
<div class="abs portrait" style="left:642px;top:855px" role="img" aria-label="Portrait of a doctor in a white coat"></div>
<div class="abs staff-name" style="left:758px;top:877px">Marcus Ellery</div>
<p class="abs staff-text" style="left:758px;top:894px;width:160px">Secondhand Smoke Linked to Raised Diabetes Risk Discovery....</p>

<footer class="abs footer"></footer>
<div class="abs foot-col" style="left:46px;top:989px"><h4>Featured Services</h4><p>Bariatric<br>Behavioral Health<br>Cancer<br>Heart<br>Kidney<br>Nasal &amp; Sinus</p></div>
<div class="abs foot-col" style="left:245px;top:989px"><h4>For Patients</h4><p>Admission<br>About Your Stay<br>Admission Process<br>Health Plans<br>Medical Records<br>Patient and Family</p></div>
<div class="abs foot-col" style="left:414px;top:989px"><h4>For Visitors</h4><p>Locations<br>Patient Guide<br>Find a Doctor<br>Visiting<br>Contact<br>Education &amp; Events</p></div>
<div class="abs foot-col address" style="left:598px;top:989px"><h4>Contact Us</h4><p>Darrel K. Holloway, MD, MBA<br>PO Box 4120 PMB 52<br>Cedar Hollow, CA 90000<br>858-555-0172<br>care@calveramd.com</p></div>
<div class="abs foot-photo" role="img" aria-label="Nurse and doctor standing with arms crossed"></div>
<div class="abs bottom">Copyright 2012 © Calvera Health Care, Inc. All Rights Reserved.</div>
</body>
</html>
```